Velvet Crest Club Members Site

To design a website template that is mobile and desktop friendly for the high net worth members, inner circle club for the rich.
Design of the website must be of luxury feel, a club for the rich.
This website offers redemption of luxury items such as travel packages, and many other items.

Below are the page templates required:

MEMBER SITE

- Login Page
- Dashboard Page (Consists of the member’s redemption points summary, expiry dates)
- Categories Page (The main categories of luxury to redeem)
- Product Page (The actual product details to redeem, showing price, description, title, remarks)
- Redemption Cart (Like a shopping cart which temporary stores the selected items for redemption)
- Checkout Page (Like shopping cart checkout to confirm redemption, fill in address, contact number, name)
- Redemption History (Show a list of items redeemed, with the redemption points used, date)
- Redemption Product Page (Show the redeem product’s details like price, description, title, remarks, date redeemed, points used)
- Inbox (Messaging towards customer service/support)
- Write Message Page
- Read Message Page
- Change Password Page
- My Profile Page

ADMIN SITE

- Login Page
- Dashboard Page (Consists of the whole system redemption points summary in the whole club)
- Redemption Page (To Approve or Cancel Redemptions, or message member to ask more about the redemption)
- Administrator List (List the admins in the system)
- Change Password Page
- Inbox (Messaging towards customer)
- Write Message Page
- Read Message Page
- My Profile Page
- Product Management -> Product List Page, Add/Remove/Edit Product Page
- Category Management -> Category List Page, Add/Remove/Edit Category Page

Note:
All colours should be easily changeable under one css file.
You are feel to use colour tones that reflect high society, rich inner circle club.
The website must be mobile friendly.

Reason: Logo of website uploaded in project brief, pls use the colours tone from the logo. Thanks.

Target Market(s)

High Networth Individuals

Industry/Entity Type

Club

Coding

Coded - Design and coding required

Number of Pages Required

5+ page

Font styles to use
Serif
Sans Serif
Decorative
Script

Requirements
Must have
• It must be desktop and mobile friendly
• All colours should be easily changeable under one css file.

```html
<!DOCTYPE html>
<html lang="en">
<head>
<meta charset="UTF-8">
<title>Velvet Crest Club – Categories</title>
<link rel="stylesheet" href="https://fonts.googleapis.com/css2?family=Oswald:wght@400;500&family=Roboto:wght@400;500&display=swap">
<style>
:root{
  --brand-dark:#3a3d44;
  --accent:#3aa3d8;
  --accent-active:#4191d0;
  --sidebar-bg:#2e303c;
  --sidebar-line:#383a47;
  --sidebar-text:#c9ccd4;
  --page-bg:#f0f0f0;
  --card-bg:#ffffff;
  --card-border:#dcdcdc;
  --text-title:#2f2f2f;
  --text-body:#6b6b6b;
  --footer-bg:#262626;
  --white:#ffffff;
}
*{box-sizing:border-box;margin:0;padding:0}
html,body{width:1036px;height:1200px;overflow:hidden}
body{font-family:"Roboto",Arial,sans-serif;background:var(--white);position:relative}

.site-header{position:absolute;left:0;top:0;width:1036px;height:82px;background:var(--white);border-bottom:1px solid #e4e4e4}
.brand{position:absolute;left:24px;top:24px;display:flex;align-items:center;gap:9px}
.brand-mark{width:10px;height:10px;background:var(--accent)}
.brand-name{font-family:"Oswald",sans-serif;font-weight:400;font-size:27px;letter-spacing:-.3px;color:var(--brand-dark);line-height:34px}
.header-actions{position:absolute;top:24px;left:678px;display:flex;gap:9px}
.btn{height:32px;width:102px;background:var(--accent);color:var(--white);border-radius:2px;display:flex;align-items:center;justify-content:center;gap:6px;font-size:13px;box-shadow:0 1px 2px rgba(0,0,0,.15)}
.btn svg{width:12px;height:12px;fill:var(--white)}

.sidebar{position:absolute;left:0;top:82px;width:232px;height:1060px;background:var(--sidebar-bg)}
.nav-item{height:49px;display:flex;align-items:center;padding-left:27px;color:var(--sidebar-text);font-size:13.5px;border-bottom:1px solid var(--sidebar-line);position:relative}
.nav-item svg.icon{width:17px;height:17px;fill:#9fa3ad;margin-right:12px}
.nav-item .chev{position:absolute;left:207px;top:19px;width:8px;height:11px;stroke:#b9bcc4;stroke-width:2;fill:none}
.nav-item.is-active{background:var(--accent-active);color:var(--white)}
.nav-item.is-active svg.icon{fill:var(--white)}
.nav-item.is-active .chev{stroke:var(--white)}

.main{position:absolute;left:232px;top:82px;width:804px;height:1060px;background:var(--page-bg)}
.hero{position:absolute;left:38px;top:26px;width:731px;height:245px;background:var(--white);border:1px solid #e2e2e2;padding:3px}
.hero-art{width:100%;height:100%;background:linear-gradient(180deg,#7fcdf0 0%,#cdeefc 55%,#e9e6d8 80%,#9bb87a 100%)}
.hero-caption{position:absolute;left:399px;top:153px;width:302px;height:80px;background:rgba(70,70,70,.72);text-align:center;color:var(--white);font-family:"Oswald",sans-serif}
.hero-caption h1{font-weight:500;font-size:29px;line-height:34px;margin-top:12px;letter-spacing:.3px}
.hero-caption p{font-size:15px;line-height:20px;letter-spacing:.1px}

.card-grid{position:absolute;left:40px;top:302px;display:grid;grid-template-columns:repeat(3,233px);column-gap:14px;row-gap:18px}
.card{height:234px;background:var(--card-bg);border:1px solid var(--card-border);padding:2px}
.card-photo{height:138px}
.card-body{padding:13px 10px 0 11px}
.card-title{font-size:12.2px;font-weight:400;color:var(--text-title);line-height:16px}
.card-text{font-size:8.8px;color:var(--text-body);line-height:15px;margin-top:4px;text-align:justify}
.card-link{font-size:8.5px;color:var(--accent);margin-top:3px;display:block}

.site-footer{position:absolute;left:0;top:1142px;width:1036px;height:58px;background:var(--footer-bg);color:#e6e6e6;font-size:11.5px}
.site-footer p{position:absolute;left:366px;top:21px}
</style>
</head>
<body>
<header class="site-header">
  <div class="brand"><span class="brand-name">VELVET CREST CLUB</span><span class="brand-mark"></span></div>
  <nav class="header-actions">
    <div class="btn"><svg viewBox="0 0 16 16"><path d="M15 1 1 7l5 2 1 6 3-4 4 3z"/></svg>Book Now</div>
    <div class="btn"><svg viewBox="0 0 16 16"><path d="M8 5a3 3 0 1 0 0 6A3 3 0 0 0 8 5zm6 2V9l-2 .4-.5 1.2 1.2 1.7-1.4 1.4-1.7-1.2-1.2.5L8 15H7l-.4-2-1.2-.5-1.7 1.2-1.4-1.4 1.2-1.7L3 9.4 1 9V7l2-.4.5-1.2-1.2-1.7 1.4-1.4 1.7 1.2 1.2-.5L7 1h2l.4 2 1.2.5 1.7-1.2 1.4 1.4-1.2 1.7.5 1.2z"/></svg>Setting</div>
    <div class="btn"><svg viewBox="0 0 16 16"><circle cx="8" cy="5" r="3.3"/><path d="M2 15c0-4 2.5-6 6-6s6 2 6 6z"/></svg>Login</div>
  </nav>
</header>

<aside class="sidebar">
  <div class="nav-item"><svg class="icon" viewBox="0 0 16 16"><path d="M8 3a7 7 0 0 0-7 7v2h14v-2a7 7 0 0 0-7-7zm-.7 8L11 5l-2.3 6.3z"/></svg>Dashboard<svg class="chev" viewBox="0 0 8 11"><path d="M1 1l5 4.5L1 10"/></svg></div>
  <div class="nav-item is-active"><svg class="icon" viewBox="0 0 16 16"><path d="M11 1l4 4-9 9H2v-4z"/></svg>Categories<svg class="chev" viewBox="0 0 8 11"><path d="M1 1l5 4.5L1 10"/></svg></div>
  <div class="nav-item"><svg class="icon" viewBox="0 0 16 16"><path d="M1 1h7l7 7-7 7-7-7zm3 2.2a1.3 1.3 0 1 0 0 2.6 1.3 1.3 0 0 0 0-2.6z"/></svg>Product<svg class="chev" viewBox="0 0 8 11"><path d="M1 1l5 4.5L1 10"/></svg></div>
  <div class="nav-item"><svg class="icon" viewBox="0 0 16 16"><path d="M1 2h14v10H1zm2 2v6h10V4zM5 13h6v2H5z"/></svg>Redemption Cart<svg class="chev" viewBox="0 0 8 11"><path d="M1 1l5 4.5L1 10"/></svg></div>
  <div class="nav-item"><svg class="icon" viewBox="0 0 16 16"><path d="M1 3h4v4H1zm5 0h9v4H6zM1 9h4v4H1zm5 0h9v4H6z"/></svg>Checkout<svg class="chev" viewBox="0 0 8 11"><path d="M1 1l5 4.5L1 10"/></svg></div>
  <div class="nav-item"><svg class="icon" viewBox="0 0 16 16"><path d="M3 1h7l3 3v11H3zm2 6v1h6V7zm0 3v1h6v-1z"/></svg>Redemption History<svg class="chev" viewBox="0 0 8 11"><path d="M1 1l5 4.5L1 10"/></svg></div>
  <div class="nav-item"><svg class="icon" viewBox="0 0 16 16"><path d="M5 1h6v5H5zM1 8h6v6H1zm8 0h6v6H9z"/></svg>Redemption Product<svg class="chev" viewBox="0 0 8 11"><path d="M1 1l5 4.5L1 10"/></svg></div>
  <div class="nav-item"><svg class="icon" viewBox="0 0 16 16"><path d="M1 3h5l1 2h8v9H1z"/></svg>Pages<svg class="chev" viewBox="0 0 8 11"><path d="M1 1l5 4.5L1 10"/></svg></div>
</aside>

<main class="main">
  <section class="hero">
    <div class="hero-art" role="img" aria-label="Travel collage of world landmarks and airplanes under a bright blue sky"></div>
    <div class="hero-caption">
      <h1>VELVET CREST CLUB</h1>
      <p>NEQUE PORRO QUISQUAM EST QUI DOLOREM</p>
    </div>
  </section>

  <section class="card-grid">
    <article class="card"><div class="card-photo" role="img" aria-label="Overwater villas above a turquoise lagoon" style="background:linear-gradient(180deg,#c9ccd0 0%,#b7b5ae 45%,#6fb8b3 70%,#4aa3a4 100%)"></div><div class="card-body"><h2 class="card-title">Neque porro quisquam</h2><p class="card-text">Lorem Ipsum has been the industry's standard dummy text ever since the 1500s, when an unknown</p><span class="card-link">Read More &gt;&gt;</span></div></article>
    <article class="card"><div class="card-photo" role="img" aria-label="Traveller in a sun hat taking a photo on a city street" style="background:linear-gradient(120deg,#c8b59c 0%,#e9d9c4 40%,#7d8fa6 75%,#8a6a52 100%)"></div><div class="card-body"><h2 class="card-title">Neque porro quisquam</h2><p class="card-text">Lorem Ipsum has been the industry's standard dummy text ever since the 1500s, when an unknown</p><span class="card-link">Read More &gt;&gt;</span></div></article>
    <article class="card"><div class="card-photo" role="img" aria-label="Resort pool with a wooden bridge among palm trees" style="background:linear-gradient(180deg,#6fa6d8 0%,#2f6a3a 35%,#8c6a48 60%,#1e9be0 100%)"></div><div class="card-body"><h2 class="card-title">Neque porro quisquam</h2><p class="card-text">Lorem Ipsum has been the industry's standard dummy text ever since the 1500s, when an unknown</p><span class="card-link">Read More &gt;&gt;</span></div></article>
    <article class="card"><div class="card-photo" role="img" aria-label="Group of friends celebrating together in a bar" style="background:linear-gradient(135deg,#9a7a5c 0%,#c9a27a 40%,#a8403a 70%,#3f6b8a 100%)"></div><div class="card-body"><h2 class="card-title">Neque porro quisquam</h2><p class="card-text">Lorem Ipsum has been the industry's standard dummy text ever since the 1500s, when an unknown</p><span class="card-link">Read More &gt;&gt;</span></div></article>
    <article class="card"><div class="card-photo" role="img" aria-label="Beach cabana and wooden boardwalk by the sea" style="background:linear-gradient(180deg,#5b9fdc 0%,#bcd7ec 40%,#d8cfc0 65%,#8b8580 100%)"></div><div class="card-body"><h2 class="card-title">Neque porro quisquam</h2><p class="card-text">Lorem Ipsum has been the industry's standard dummy text ever since the 1500s, when an unknown</p><span class="card-link">Read More &gt;&gt;</span></div></article>
    <article class="card"><div class="card-photo" role="img" aria-label="Friends jumping on a coastal road at sunset" style="background:linear-gradient(180deg,#f2d7a8 0%,#e9c08a 40%,#b86b4e 70%,#5a7f9c 100%)"></div><div class="card-body"><h2 class="card-title">Neque porro quisquam</h2><p class="card-text">Lorem Ipsum has been the industry's standard dummy text ever since the 1500s, when an unknown</p><span class="card-link">Read More &gt;&gt;</span></div></article>
    <article class="card"><div class="card-photo" role="img" aria-label="Palm tree over a tropical resort pool at dusk" style="background:linear-gradient(180deg,#cfe4dc 0%,#9ac2c0 40%,#b56a5a 55%,#1677c8 100%)"></div><div class="card-body"><h2 class="card-title">Neque porro quisquam</h2><p class="card-text">Lorem Ipsum has been the industry's standard dummy text ever since the 1500s, when an unknown</p><span class="card-link">Read More &gt;&gt;</span></div></article>
    <article class="card"><div class="card-photo" role="img" aria-label="City skyline and yacht marina at golden hour" style="background:linear-gradient(180deg,#d9c7a4 0%,#a89b86 40%,#6f757c 70%,#b9bcc0 100%)"></div><div class="card-body"><h2 class="card-title">Neque porro quisquam</h2><p class="card-text">Lorem Ipsum has been the industry's standard dummy text ever since the 1500s, when an unknown</p><span class="card-link">Read More &gt;&gt;</span></div></article>
    <article class="card"><div class="card-photo" role="img" aria-label="Luxury villa pavilion beside a pool with palms" style="background:linear-gradient(180deg,#9fd0ee 0%,#8a5a42 45%,#e6dccb 70%,#4f9a8a 100%)"></div><div class="card-body"><h2 class="card-title">Neque porro quisquam</h2><p class="card-text">Lorem Ipsum has been the industry's standard dummy text ever since the 1500s, when an unknown</p><span class="card-link">Read More &gt;&gt;</span></div></article>
  </section>
</main>

<footer class="site-footer"><p>Copyright © 2016. All Rights Reserved.</p></footer>
</body>
</html>
```